Harrowgate Estates Business Card for Apartment Buildings

Create business cards for resident managers who run apartment buildings. The audience is the public who are searching for apartment rentals, and current residents who live at the apartment building. Key design element will be incorporating the company logo, however, the logo cannot dominate. The building name and manager name are more important than the logo. Current business card design leaves little room for copy, so we may need to reduce the size on the current card to allow for more space for copy.

Target Market(s)

Adults 18-65 years of age, who are looking for an apartment rental, plus current residents who live at our apartment buildings.

Industry/Entity Type

Property Management

Contact Information for Business Card

A major design element will be use of the company logo. Important property and manager contact information must be part of the design. The size of the logo will need to be reduced to make room for building and manager contact copy.

Font styles to use
Sans Serif

Colors
3176b5
000000
959595
ffffff

Requirements
Must have
• 1) Incorporate the company logo.
• 2) Use the company colors (dark blue, black/grey, over white).
• 3) FEATURE THE BUILDING NAME
• 4) FEATURE THE MANAGER NAME
• 5) The company name is less important than BUILDING and MANAGER
• 6) Manager contact information
• **SEE ATTACHED CREATIVE BRIEF**
Nice to have
• 1) Back of card logo watermark
• 2) Ability to write notes on back of carfd
Should not have
• Avoid letting the company logo dominate the card, the building name and manager are more important than the company logo.

```html
<!DOCTYPE html>
<html lang="en">
<head>
<meta charset="utf-8">
<title>Harrowgate Estates – Business Card</title>
<link href="https://fonts.googleapis.com/css2?family=Montserrat:wght@400;500;600;700&display=swap" rel="stylesheet">
<style>
  :root{
    --brand-blue:#3176b5;
    --ink:#1f1f21;
    --black:#000000;
    --grey:#959595;
    --white:#ffffff;
    --rule:#9cc0e2;
    --stage:#26282c;
  }
  *{margin:0;padding:0;box-sizing:border-box}
  html,body{width:1200px;height:900px;overflow:hidden;background:var(--stage)}
  body{font-family:"Montserrat",sans-serif;position:relative}

  .card{position:absolute;width:560px;height:320px;border-radius:22px;overflow:hidden;background:var(--white)}
  .card--front{left:60px;top:290px}
  .card--back{left:640px;top:290px}

  .brand{position:absolute;left:34px;top:30px;display:flex;align-items:center;gap:10px;
    font-weight:700;font-size:20px;color:var(--brand-blue);letter-spacing:.5px;text-transform:uppercase}
  .brand__mark{width:18px;height:18px;background:var(--brand-blue);border-radius:50%}

  /* front */
  .front__dark{position:absolute;left:0;right:0;top:112px;bottom:0;background:var(--ink)}
  .front__building{position:absolute;left:260px;right:0;top:112px;height:46px;background:var(--brand-blue);
    border-top-left-radius:26px;color:var(--white);font-weight:600;font-size:15.5px;letter-spacing:.8px;
    display:flex;align-items:center;padding-left:24px;white-space:nowrap;text-transform:uppercase}
  .front__notch{position:absolute;right:0;top:88px;width:110px;height:26px;background:var(--brand-blue);
    border-top-left-radius:18px}
  .front__edge{position:absolute;left:0;bottom:0;width:130px;height:10px;background:var(--brand-blue)}

  .manager{position:absolute;left:34px;top:130px;width:210px;color:var(--white)}
  .manager__name{font-weight:600;font-size:17px;letter-spacing:1.2px;text-transform:uppercase;white-space:nowrap}
  .manager__role{font-size:11px;color:var(--grey);margin-top:5px}

  .contacts{position:absolute;left:240px;top:176px;border-left:1.5px solid var(--brand-blue);
    padding-left:18px;list-style:none;color:var(--white);font-size:13px;line-height:21px}
  .contacts li{display:flex;align-items:center;gap:9px;white-space:nowrap}
  .contacts svg{width:12px;height:12px;flex:none;fill:var(--brand-blue)}
  .address{position:absolute;left:240px;top:274px;color:var(--white);font-size:13.5px;white-space:nowrap}

  /* back */
  .notes{position:absolute;left:80px;right:50px;top:96px}
  .notes__line{height:1px;background:var(--rule);margin-bottom:30px}
  .back__tab-left{position:absolute;left:0;bottom:0;width:150px;height:16px;background:var(--brand-blue);border-top-right-radius:14px}
  .back__tab-right{position:absolute;right:0;top:0;width:190px;height:14px;background:var(--brand-blue);border-bottom-left-radius:14px}
</style>
</head>
<body>

<section class="card card--front" aria-label="Card front">
  <div class="brand"><span class="brand__mark"></span>Harrowgate Estates</div>
  <div class="front__notch"></div>
  <div class="front__dark"></div>
  <div class="front__building">Linden Court Apartments</div>
  <div class="front__edge"></div>

  <div class="manager">
    <div class="manager__name">Owen Marlowe</div>
    <div class="manager__role">General Manager</div>
  </div>

  <ul class="contacts">
    <li><svg viewBox="0 0 24 24"><path d="M6.6 10.8a15 15 0 0 0 6.6 6.6l2.2-2.2a1 1 0 0 1 1-.25 11.4 11.4 0 0 0 3.6.57 1 1 0 0 1 1 1V20a1 1 0 0 1-1 1A17 17 0 0 1 3 4a1 1 0 0 1 1-1h3.5a1 1 0 0 1 1 1c0 1.25.2 2.450.57 3.57a1 1 0 0 1-.25 1z"/></svg>00 2468 135 790</li>
    <li><svg viewBox="0 0 24 24"><rect x="2" y="2" width="20" height="20" rx="3"/></svg>00 2468 135 791</li>
    <li><svg viewBox="0 0 24 24"><path d="M2 5h20v14H2z M2 5l10 8 10-8" stroke="#1f1f21" stroke-width="1.5"/></svg>yourmail@harrowgateestates.com</li>
    <li><svg viewBox="0 0 24 24"><circle cx="12" cy="12" r="10"/></svg>www.harrowgateestates.com</li>
  </ul>
  <div class="address">48 Fenwick Row, Leeds, UK</div>
</section>

<section class="card card--back" aria-label="Card back with note lines">
  <div class="back__tab-right"></div>
  <div class="brand"><span class="brand__mark"></span>Harrowgate Estates</div>
  <div class="notes">
    <div class="notes__line"></div>
    <div class="notes__line"></div>
    <div class="notes__line"></div>
    <div class="notes__line"></div>
    <div class="notes__line"></div>
    <div class="notes__line"></div>
  </div>
  <div class="back__tab-left"></div>
</section>

</body>
</html>
```